Cd Cover design for Chicago based record label.

Cd Cover design for a new single! Song is dedicated to exotic dancers. We do not want our artist pictures on this one. So please use your imagination. Song Title: "Velvet Hours". Thanks? Artist: Ray Castellan feat. Lil Trevane.

```html
<!DOCTYPE html>
<html lang="en">
<head>
<meta charset="utf-8">
<title>Velvet Hours – Single Cover</title>
<link href="https://fonts.googleapis.com/css2?family=Rubik+Dirt&family=Quicksand:wght@500&display=swap" rel="stylesheet">
<style>
  :root {
    --page-bg: #d9d9db;
    --cover-white: #fbfafc;
    --orchid: #b23fb0;
    --violet: #6b2d8f;
    --magenta: #d6338f;
    --haze: #e9d8ec;
    --ink: #15151a;
    --navy: #262a3f;
  }
  html, body {
    margin: 0;
    width: 1200px;
    height: 960px;
    overflow: hidden;
    background: var(--page-bg);
  }
  .cover {
    position: absolute;
    left: 180px;
    top: 60px;
    width: 840px;
    height: 840px;
    background: var(--cover-white);
    overflow: hidden;
    box-shadow: 0 6px 24px rgba(0,0,0,0.18);
  }
  .dancer-art {
    position: absolute;
    inset: 0;
    background:
      radial-gradient(ellipse 22% 20% at 52% 26%, var(--violet) 0%, rgba(107,45,143,0.85) 45%, transparent 100%),
      radial-gradient(ellipse 34% 16% at 44% 14%, rgba(178,63,176,0.85) 0%, transparent 100%),
      radial-gradient(ellipse 30% 40% at 50% 48%, rgba(214,51,143,0.55) 0%, transparent 100%),
      linear-gradient(115deg, transparent 48%, rgba(214,51,143,0.7) 50%, rgba(214,51,143,0.7) 54%, transparent 56%),
      radial-gradient(ellipse 60% 30% at 55% 82%, rgba(178,63,176,0.5) 0%, transparent 100%),
      radial-gradient(ellipse 45% 35% at 18% 40%, var(--haze) 0%, transparent 100%),
      var(--cover-white);
  }
  .title {
    position: absolute;
    left: 250px;
    top: 70px;
    margin: 0;
    transform-origin: left top;
    transform: rotate(62deg);
    font-family: "Rubik Dirt", cursive;
    font-weight: 400;
    color: var(--ink);
    line-height: 0.9;
    white-space: nowrap;
  }
  .title-small { display: block; font-size: 78px; }
  .title-large { display: block; font-size: 176px; letter-spacing: 4px; }
  .credit-strip {
    position: absolute;
    right: 40px;
    top: 150px;
    bottom: 40px;
    width: 40px;
    display: flex;
    flex-direction: column;
    align-items: center;
    gap: 20px;
  }
  .credit-bar {
    width: 14px;
    background: var(--navy);
  }
  .credit-bar--short { height: 52px; flex: none; }
  .credit-bar--long { flex: 1; }
  .credits {
    flex: none;
    margin: 0;
    writing-mode: vertical-rl;
    transform: rotate(180deg);
    font-family: "Quicksand", sans-serif;
    font-weight: 500;
    font-size: 26px;
    line-height: 1;
    color: var(--navy);
    white-space: nowrap;
  }
</style>
</head>
<body>
  <main class="cover">
    <div class="dancer-art" role="img" aria-label="Grunge-textured illustration of a dancer silhouette on a pole in violet and magenta tones"></div>
    <h1 class="title">
      <span class="title-small">Velvet</span>
      <span class="title-large">Hours</span>
    </h1>
    <div class="credit-strip">
      <div class="credit-bar credit-bar--short"></div>
      <p class="credits">Ray Castellan feat. Lil Trevane</p>
      <div class="credit-bar credit-bar--long"></div>
    </div>
  </main>
</body>
</html>
```